Wedding Photo Studio needs custom webpage

I'm changing up my service offering to offer multiple editing styles. I'm looking to update my website to reflect that but still showcase my dreamy edits as an attention grabbing part of the website.

I will have 4 color editing styles (Colm's Hallmark, Bright & Airy, Silken Oak, Dreamy) and one black and white style. I have attached sample images in each style.

I also attached a couple dreamy edits that can be used as attention grabbing images.

I'm hoping for some functionality that perhaps takes a single image and divides it by 4 to show 25% in each style that can be clicked on and would 'maximize' the carousel to that style but still have a functionality to go to a different style after being maximized.

You can see www.colmvphotography.com for the current design and content. It doesn't have to be too different (but can be). It just needs to showcase the multiple editing styles effectively.

Target Market(s)

Couples who are having $20-50k weddings.

Industry/Entity Type

Photography

Coding

Coded - Design and coding required

Number of Pages Required

3 page

Colors

Designer to choose colors to be used in the design.

Requirements
Must have
• Pricing page with toggles for (off-season/on-season, Saturday/non-saturday) accurate pricing, good way to show multiple editing style photos.

```html
<!DOCTYPE html>
<html lang="en">
<head>
<meta charset="utf-8">
<title>Colm V Photography</title>
<link href="https://fonts.googleapis.com/css2?family=Open+Sans:wght@400;600;700;800&family=Lora:wght@400&family=Roboto:wght@400;500;700&display=swap" rel="stylesheet">
<style>
:root{
  --blue:#0b3d91;
  --blue-dark:#08306f;
  --pale:#e8f0f8;
  --pale-2:#dde7f2;
  --ink:#111111;
  --text:#333333;
  --muted:#666666;
  --white:#ffffff;
  --black:#000000;
  --star:#f08a00;
}
*{margin:0;padding:0;box-sizing:border-box}
html,body{width:1200px;height:4769px;overflow:hidden;background:var(--white)}
body{font-family:"Open Sans",sans-serif;color:var(--text)}
.page{position:relative;width:1200px;height:4769px;overflow:hidden}
.abs{position:absolute}
.brand{font-family:"Open Sans",sans-serif;font-weight:700;color:var(--blue);display:flex;align-items:center;gap:10px}
.brand .dot{width:14px;height:14px;border-radius:50%;background:var(--blue)}

/* header */
.site-header{left:0;top:0;width:1200px;height:86px;background:var(--white)}
.site-header .brand{position:absolute;left:110px;top:26px;font-size:26px}
.main-nav{position:absolute;left:490px;top:31px;display:flex;gap:0;font-size:15px;color:#333}
.main-nav span{position:absolute;white-space:nowrap}
.nav-active{color:var(--blue);font-weight:700}
.btn-contact{position:absolute;left:956px;top:20px;width:132px;height:46px;background:var(--blue);color:#fff;font-weight:700;font-size:15px;display:flex;align-items:center;justify-content:center;box-shadow:0 2px 6px rgba(0,0,0,.3)}

/* hero */
.hero{left:0;top:86px;width:1200px;height:594px;background:linear-gradient(180deg,#3b3552 0%,#7c4a66 30%,#b5584a 52%,#3a2b3a 75%,#1c1a24 100%)}
.hero-copy{left:111px;top:150px;color:#fff}
.hero-kicker{font-size:31px;font-weight:600}
.hero-title{font-size:42px;font-weight:700;margin-top:8px;letter-spacing:.5px}
.hero-text{font-family:"Lora",serif;font-size:14.5px;line-height:31px;width:450px;margin-top:4px}
.btn-start{display:inline-flex;margin-top:16px;width:132px;height:46px;background:var(--blue);color:#fff;font-size:14px;font-weight:700;align-items:center;justify-content:center}
.arrow{width:18px;height:30px}

/* about */
.about-frame{left:130px;top:785px;width:400px;height:328px;background:var(--pale-2)}
.about-photo{left:174px;top:830px;width:400px;height:408px;background:linear-gradient(135deg,#6a2020 0%,#b03a30 30%,#e8d8d0 60%,#2a2a30 100%)}
.about-title{left:645px;top:792px;font-size:31px;font-weight:700;color:var(--ink)}
.about-text{left:645px;top:862px;width:450px;font-family:"Lora",serif;font-size:14.5px;line-height:31px;color:#333}
.about-text p+p{margin-top:34px}
.about-sign{left:645px;top:1170px;font-size:30px}

/* sections */
.pale-band{background:var(--pale)}
.section-title{width:1200px;text-align:center;font-size:31px;font-weight:700;color:var(--ink)}
.title-rule{left:575px;width:50px;height:3px;background:var(--blue)}

.style-card{width:309px;height:278px;background:#fff;border-radius:10px;overflow:hidden;box-shadow:0 2px 8px rgba(0,0,0,.12)}
.style-card .img{height:222px}
.style-card .label{height:56px;display:flex;align-items:center;justify-content:center;font-weight:700;font-size:17px;color:var(--ink)}

.panel{top:2322px;height:480px}
.panel-active{left:600px;top:2305px;width:245px;height:520px;background:linear-gradient(180deg,#2a1f1a,#5a4035 55%,#2a1e18);box-shadow:0 0 12px rgba(0,0,0,.35)}
.panel-active .label{position:absolute;left:0;width:245px;top:420px;text-align:center;color:#fff;font-weight:700;font-size:20px}

.testi{width:310px;height:330px;background:#fff;border-radius:8px;box-shadow:0 2px 10px rgba(0,0,0,.1);padding:20px 25px}
.stars{color:var(--star);font-size:15px;letter-spacing:1px}
.testi p{font-family:"Roboto",sans-serif;font-size:13.3px;line-height:25.5px;color:#333;text-align:justify;margin-top:6px;height:160px}
.testi hr{border:0;border-top:2px solid #ccc;margin:10px 0 22px;width:258px}
.who{display:flex;align-items:center;gap:16px}
.avatar{width:56px;height:56px;border-radius:50%;background:linear-gradient(135deg,#c9b8b0,#5a4a48)}
.who b{display:block;font-family:"Roboto",sans-serif;font-weight:500;font-size:18px;color:var(--ink)}
.who span{font-family:"Roboto",sans-serif;font-size:15px;color:#444}

.price-card{top:3716px;width:422px;height:467px;background:#fff;border-radius:12px;overflow:hidden;box-shadow:0 2px 12px rgba(0,0,0,.12)}
.price-head{position:absolute;left:0;top:0;width:422px;height:180px;color:#fff;text-align:center;font-family:"Roboto",sans-serif}
.price-head .season{position:absolute;top:34px;width:100%;font-size:15px;font-weight:500}
.price-head .amount{position:absolute;top:58px;width:100%;font-size:34px;font-weight:700}
.price-head .day{position:absolute;top:118px;width:100%;font-size:15px;font-weight:500}
.features{position:absolute;left:36px;top:195px;list-style:none;font-family:"Roboto",sans-serif;font-size:15.5px;color:#333}
.features li{display:flex;align-items:center;gap:20px;height:41px}
.tick{width:17px;height:17px;border-radius:50%;background:#111;display:flex;align-items:center;justify-content:center}
.btn-trial{position:absolute;left:126px;top:407px;width:170px;height:42px;background:var(--pale-2);color:var(--blue);font-family:"Roboto",sans-serif;font-weight:500;font-size:16px;display:flex;align-items:center;justify-content:center}

.site-footer{left:0;top:4290px;width:1200px;height:479px;background:var(--black);color:#fff}
.foot-nav{position:absolute;top:245px;left:0;width:1200px;font-size:15px}
.foot-nav span{position:absolute;white-space:nowrap}
.contact-item{position:absolute;top:295px;display:flex;align-items:center;gap:22px;font-size:15px}
.contact-icon{width:50px;height:50px;background:var(--blue);display:flex;align-items:center;justify-content:center}
.copyright{position:absolute;top:392px;width:1200px;text-align:center;font-size:15px}
.copyright em{font-style:normal;color:#2d6fd6}
</style>
</head>
<body>
<div class="page">

<header class="site-header abs">
  <div class="brand"><span class="dot"></span>Colm V Photography</div>
  <nav class="main-nav">
    <span class="nav-active" style="left:0">HOME</span>
    <span style="left:82px">THE TEAM</span>
    <span style="left:192px">PORTFOLIO</span>
    <span style="left:312px">BLOG</span>
    <span style="left:389px">PRICING</span>
  </nav>
  <div class="btn-contact">CONTACT ME</div>
</header>

<section class="hero abs" role="img" aria-label="Couple kissing in front of a sunset lake">
</section>
<div class="hero-copy abs" style="top:236px">
  <div class="hero-kicker">WELCOME TO</div>
  <div class="hero-title">COLM V PHOTOGRAPHY</div>
  <p class="hero-text">I am an accountant by day, photographer by night. I once read a happy life is had by loving your job, loving your creative hobby and the love of family;</p>
  <div class="btn-start">GET STARTED</div>
</div>
<svg class="abs arrow" style="left:50px;top:333px" viewBox="0 0 18 30"><path d="M15 2 3 15l12 13" fill="none" stroke="#fff" stroke-width="2"/></svg>
<svg class="abs arrow" style="left:1132px;top:333px" viewBox="0 0 18 30"><path d="M3 2l12 13L3 28" fill="none" stroke="#fff" stroke-width="2"/></svg>
<svg class="abs" style="left:0;top:625px" width="1200" height="60" viewBox="0 0 1200 60">
  <polygon points="0,60 1200,10 1200,60" fill="#fff"/>
  <polygon points="440,38 1200,8 1200,28 470,42" fill="var(--blue)"/>
  <polygon points="0,60 1200,28 1200,60" fill="#fff"/>
</svg>

<section class="about">
  <div class="about-frame abs"></div>
  <div class="about-photo abs" role="img" aria-label="Groom kissing bride's forehead beside red autumn trees"></div>
  <h2 class="about-title abs">ABOUT ME</h2>
  <div class="about-text abs">
    <p>I am an accountant by day, photographer by night. I once read a happy life is had by loving your job, loving your creative hobby and the love of family; photography is one part of that for me. I focus primarily on wedding photography in southern Ontario.</p>
    <p>I cover Toronto, Hamilton, Kitchener, Waterloo, London and anywhere in the world you want to send me. If you like what I do, please reach out; I'm happy to meet with you and chat more about your big day.</p>
  </div>
  <div class="about-sign abs brand"><span class="dot"></span>Colm V</div>
</section>

<section class="pale-band abs" style="left:0;top:1345px;width:1200px;height:860px"></section>
<svg class="abs" style="left:0;top:1340px" width="1200" height="50" viewBox="0 0 1200 50">
  <polygon points="0,0 1200,0 1200,5 0,45" fill="#fff"/>
  <polygon points="0,28 760,4 0,45" fill="var(--blue)"/>
</svg>
<h2 class="section-title abs" style="left:0;top:1446px">OUR EDITING STYLES</h2>
<div class="title-rule abs" style="top:1498px"></div>

<div class="style-card abs" style="left:111px;top:1533px"><div class="img" role="img" aria-label="Couple under a lit venue entrance at night, dreamy edit" style="background:linear-gradient(180deg,#1a1d33,#c0562a 55%,#3a2a28)"></div><div class="label">DREAMY</div></div>
<div class="style-card abs" style="left:445px;top:1533px"><div class="img" role="img" aria-label="Couple walking by a waterfall, silken oak edit" style="background:linear-gradient(180deg,#6a5a48,#9c8468 55%,#4e4034)"></div><div class="label">SILKEN OAK</div></div>
<div class="style-card abs" style="left:780px;top:1533px"><div class="img" role="img" aria-label="Couple walking by a waterfall, bright and airy edit" style="background:linear-gradient(180deg,#a9b4a4,#d9dcd4 55%,#7f8a74)"></div><div class="label">BRIGHT &amp; AIRY</div></div>
<div class="style-card abs" style="left:278px;top:1834px"><div class="img" role="img" aria-label="Couple walking in autumn garden, signature edit" style="background:linear-gradient(180deg,#5c6a48,#c48a3e 50%,#4a3e30)"></div><div class="label">COLM'S HALLMARK</div></div>
<div class="style-card abs" style="left:613px;top:1834px"><div class="img" role="img" aria-label="Couple walking in garden, black and white edit" style="background:linear-gradient(180deg,#555,#bbb 50%,#333)"></div><div class="label">BLACK AND WHITE</div></div>

<div class="panel abs" style="left:111px;width:245px;background:linear-gradient(180deg,#0d0d0d,#3a3a3a 50%,#111)" role="img" aria-label="Guests dancing, black and white edit"></div>
<div class="panel abs" style="left:356px;width:244px;background:linear-gradient(180deg,#1a1a1a,#7a7a7a 50%,#222)" role="img" aria-label="Groom cheering on the dance floor"></div>
<div class="panel abs" style="left:845px;width:243px;background:linear-gradient(180deg,#222,#9a9a9a 50%,#2a2a2a)" role="img" aria-label="Guests dancing and celebrating"></div>
<div class="panel-active abs" role="img" aria-label="Bride dancing, dreamy edit"><div class="label">DREAMY</div></div>

<section class="pale-band abs" style="left:0;top:2920px;width:1200px;height:632px"></section>
<svg class="abs" style="left:0;top:2918px" width="1200" height="50" viewBox="0 0 1200 50">
  <polygon points="0,0 1200,0 1200,45 0,2" fill="#fff"/>
  <polygon points="440,20 1200,28 1200,45" fill="var(--blue)"/>
</svg>
<h2 class="section-title abs" style="left:0;top:3018px">TESTIMONIALS</h2>
<div class="title-rule abs" style="top:3070px"></div>
<svg class="abs arrow" style="left:50px;top:3263px" viewBox="0 0 18 30"><path d="M15 2 3 15l12 13" fill="none" stroke="#999" stroke-width="2"/></svg>
<svg class="abs arrow" style="left:1132px;top:3263px" viewBox="0 0 18 30"><path d="M3 2l12 13L3 28" fill="none" stroke="#333" stroke-width="2"/></svg>

<div class="testi abs" style="left:111px;top:3115px">
  <div class="stars">★★★★★</div>
  <p>Colm is the absolute best! He did a SPECTACULAR job with our wedding photos. He got images of everything, even the things that we never thought he would notice. Hands down Colm is the best you will not be disappointed.</p>
  <hr>
  <div class="who"><div class="avatar"></div><div><b>Mira &amp; Joel</b><span>Southern Ontario.</span></div></div>
</div>
<div class="testi abs" style="left:445px;top:3115px">
  <div class="stars">★★★★★</div>
  <p>We got married September 30 and hired Colm and we are VERY HAPPY we did! Colm did an AMAZING job!! He is very professional, very organized, got the most beautiful shots, he captured the all the most important beautiful ways</p>
  <hr>
  <div class="who"><div class="avatar"></div><div><b>Sam &amp; Nadia</b><span>Southern Ontario.</span></div></div>
</div>
<div class="testi abs" style="left:780px;top:3115px">
  <div class="stars">★★★★★</div>
  <p>Colm did an outstanding job on our wedding photos! We got so so much more for so so much less. Thanks again Colm, you exceeded our expectations and then some. I recommend him 100 times over!</p>
  <hr>
  <div class="who"><div class="avatar"></div><div><b>Theo &amp; Lena</b><span>Southern Ontario.</span></div></div>
</div>

<h2 class="section-title abs" style="left:0;top:3628px">OUR PRICING</h2>
<div class="title-rule abs" style="top:3678px"></div>

<div class="price-card abs" style="left:150px">
  <svg class="abs" style="left:0;top:0" width="422" height="180" viewBox="0 0 422 180"><path d="M0 0H422V90C340 200 90 200 0 90Z" fill="var(--blue)"/></svg>
  <div class="price-head"><div class="season">OFF-SEASON</div><div class="amount">$185.00</div><div class="day">SATURDAY</div></div>
  <ul class="features">
    <li><span class="tick"><svg width="9" height="8" viewBox="0 0 9 8"><path d="M1 4l2.5 2.5L8 1" fill="none" stroke="#fff" stroke-width="1.8"/></svg></span>Lorem ipsum dolor sit amet, consectetur</li>
    <li><span class="tick"><svg width="9" height="8" viewBox="0 0 9 8"><path d="M1 4l2.5 2.5L8 1" fill="none" stroke="#fff" stroke-width="1.8"/></svg></span>Duis aute irure dolor in reprehenderit</li>
    <li><span class="tick"><svg width="9" height="8" viewBox="0 0 9 8"><path d="M1 4l2.5 2.5L8 1" fill="none" stroke="#fff" stroke-width="1.8"/></svg></span>Excepteur sint occaecat cupidatat non</li>
    <li><span class="tick"><svg width="9" height="8" viewBox="0 0 9 8"><path d="M1 4l2.5 2.5L8 1" fill="none" stroke="#fff" stroke-width="1.8"/></svg></span>Nemo enim ipsam voluptatem quia voluptas</li>
    <li><span class="tick"><svg width="9" height="8" viewBox="0 0 9 8"><path d="M1 4l2.5 2.5L8 1" fill="none" stroke="#fff" stroke-width="1.8"/></svg></span>Nam libero tempore, cum soluta</li>
  </ul>
  <div class="btn-trial">Start Free Trial</div>
</div>
<div class="price-card abs" style="left:632px">
  <svg class="abs" style="left:0;top:0" width="422" height="180" viewBox="0 0 422 180"><path d="M0 0H422V90C340 200 90 200 0 90Z" fill="var(--blue)"/></svg>
  <div class="price-head"><div class="season">ON-SEASON</div><div class="amount">$185.00</div><div class="day">NON-SATURDAY</div></div>
  <ul class="features">
    <li><span class="tick"><svg width="9" height="8" viewBox="0 0 9 8"><path d="M1 4l2.5 2.5L8 1" fill="none" stroke="#fff" stroke-width="1.8"/></svg></span>Lorem ipsum dolor sit amet, consectetur</li>
    <li><span class="tick"><svg width="9" height="8" viewBox="0 0 9 8"><path d="M1 4l2.5 2.5L8 1" fill="none" stroke="#fff" stroke-width="1.8"/></svg></span>Duis aute irure dolor in reprehenderit</li>
    <li><span class="tick"><svg width="9" height="8" viewBox="0 0 9 8"><path d="M1 4l2.5 2.5L8 1" fill="none" stroke="#fff" stroke-width="1.8"/></svg></span>Excepteur sint occaecat cupidatat non</li>
    <li><span class="tick"><svg width="9" height="8" viewBox="0 0 9 8"><path d="M1 4l2.5 2.5L8 1" fill="none" stroke="#fff" stroke-width="1.8"/></svg></span>Nemo enim ipsam voluptatem quia voluptas</li>
    <li><span class="tick"><svg width="9" height="8" viewBox="0 0 9 8"><path d="M1 4l2.5 2.5L8 1" fill="none" stroke="#fff" stroke-width="1.8"/></svg></span>Nam libero tempore, cum soluta</li>
  </ul>
  <div class="btn-trial">Start Free Trial</div>
</div>

<footer class="site-footer abs">
  <div class="brand" style="position:absolute;left:0;width:1200px;top:125px;justify-content:center;color:#fff;font-size:34px"><span class="dot" style="background:#fff"></span>Colm V Photography</div>
  <nav class="foot-nav">
    <span style="left:280px">HOME</span>
    <span style="left:374px">THE TEAM</span>
    <span style="left:495px">PORTFOLIO</span>
    <span style="left:628px">BLOG</span>
    <span style="left:717px">PRICING</span>
    <span style="left:824px">CONTACT US</span>
  </nav>
  <div class="contact-item" style="left:145px"><span class="contact-icon"><svg width="22" height="16" viewBox="0 0 22 16"><rect x="1" y="1" width="20" height="14" fill="#fff"/><path d="M1 1l10 8 10-8" fill="none" stroke="var(--blue)" stroke-width="1.8"/></svg></span>info@companyname.com</div>
  <div class="contact-item" style="left:497px"><span class="contact-icon"><svg width="16" height="22" viewBox="0 0 16 22"><path d="M8 0a8 8 0 0 1 8 8c0 6-8 14-8 14S0 14 0 8a8 8 0 0 1 8-8z" fill="#fff"/><circle cx="8" cy="8" r="3" fill="var(--blue)"/></svg></span>Company Name,United State.</div>
  <div class="contact-item" style="left:853px"><span class="contact-icon"><svg width="20" height="20" viewBox="0 0 20 20"><path d="M4 1l4 4-2 3c1 2 4 5 6 6l3-2 4 4-3 3C8 19 1 12 1 4z" fill="#fff"/></svg></span>+1888 8888 888</div>
  <div class="copyright">Copyrights@2025.<em>Colm Varga Photography</em>.All Rights Reserved</div>
</footer>
<svg class="abs" style="left:0;top:4285px" width="1200" height="50" viewBox="0 0 1200 50">
  <polygon points="0,0 1200,0 1200,5 0,45" fill="#fff"/>
  <polygon points="0,28 760,4 0,45" fill="var(--blue)"/>
</svg>

</div>
</body>
</html>
```